Meadow Voyages Web Page Redesign

IF YOu ARE IN INDIA - PLEASE PLEASE PLEASE - make sure you are working off of MEADOWVOYAGES.COM - Not another site. Look at the URL above when you see the site!

Our website http://www.meadowvoyages.com is driven by a backend database providing content. We are interested in redesigning the website layout to make it responsive and also to make it more interesting, catchy and call to action oriented. Right now it seems not to be able to deliver the message and a little crowded. The main template pages to be addressed are index.aspx, default.aspx, TourList1.aspx, and the actual tour detail page.

There needs to be tight integration / prominent visibility for Social Media.

Focus needs to be on design that would reduce the bounce rate and be SEO friendly.

You will be responsible for layout and delivering the front end css / layout / slices to integrate with the back end.
Updates

If you are based in India, you are probably going to be redirected to another site. Please make sure you are working off of MEADOWVOYAGES.COM

Target Market(s)

It is a B2C site - travelers who are interested in traveling to India, Europe and South Africa.

Industry/Entity Type

Media

Font styles to use
Sans Serif

Requirements
Must have
• ONE VERY IMPORTANT POINT : We have a number of photographs that we would love to put online. Unfortunately our current design requires us to resize / crop the photographs which make them lose the impact. We would prefer a design where the images could be used as-is.

Tight integration with Social Media is there in our engine so it should be visible on the website.

Responsive.
Nice to have
• Try using the same color scheme but we are open for changes in the same tone..

```html
<!DOCTYPE html>
<html lang="en">
<head>
<meta charset="utf-8">
<title>Meadow Voyages</title>
<link href="https://fonts.googleapis.com/css2?family=Roboto:wght@100;300;400;500;700&family=Roboto+Condensed:wght@700&display=swap" rel="stylesheet">
<style>
:root{
  --topbar:#232021;
  --nav:#4a1511;
  --band:#9c4646;
  --yellow:#f6c900;
  --text:#333;
  --muted:#aaa;
  --white:#fff;
  --rule:#ddd;
}
*{margin:0;padding:0;box-sizing:border-box}
html,body{width:821px;height:1200px;overflow:hidden;background:var(--white);font-family:"Roboto",sans-serif;color:var(--text)}
.page{position:relative;width:821px;height:1200px}
.topbar{position:absolute;top:0;left:0;width:821px;height:22px;background:var(--topbar);color:#ddd;font-size:9.5px;line-height:22px;padding-left:21px}
.topbar .social{position:absolute;right:19px;top:0;display:flex;gap:26px;font-size:8.5px;letter-spacing:.4px;color:var(--muted)}
.nav{position:absolute;top:22px;left:0;width:821px;height:46px;background:var(--nav);color:var(--white)}
.brand{position:absolute;left:23px;top:11px;font-family:"Roboto Condensed",sans-serif;font-weight:700;font-size:21px;letter-spacing:.2px;white-space:nowrap}
.menu{position:absolute;left:228px;top:17px;display:flex;gap:19px;font-size:11px;font-weight:700}
.member{position:absolute;left:464px;top:18px;font-size:10.5px;color:#ccc}
.member b{font-weight:400;color:var(--white);margin-left:5px}
.offers{position:absolute;left:681px;top:9px;width:125px;height:28px;background:var(--yellow);color:#2a1b00;font-family:"Roboto Condensed",sans-serif;font-weight:700;font-size:15px;text-align:center;line-height:28px;border-radius:2px}
.hero{position:absolute;top:68px;left:0;width:821px;height:560px;background:radial-gradient(ellipse at 50% 45%,#b98a52 0%,#9a7045 35%,#7b6a45 65%,#5f6b3a 100%)}
.hero-title{position:absolute;top:222px;left:0;width:821px;text-align:center;font-weight:100;font-size:88px;line-height:100px;color:var(--white);letter-spacing:-2px}
.dots{position:absolute;top:345px;left:382px;display:flex;gap:10px}
.dots span{width:6px;height:6px;border-radius:50%;background:var(--white)}
.price{position:absolute;left:660px;top:465px;color:var(--white)}
.price small{display:block;font-size:18px;font-weight:400;line-height:22px}
.price strong{display:block;font-size:46px;font-weight:500;line-height:50px;letter-spacing:-1px}
.signup{position:absolute;top:628px;left:0;width:821px;height:88px;background:var(--band)}
.signup p{position:absolute;left:51px;top:31px;font-size:16px;font-weight:300;color:var(--white)}
.signup .field{position:absolute;left:440px;top:24px;width:247px;height:30px;background:var(--white);border:1px solid #ccc;font-size:11px;color:#999;line-height:28px;padding-left:7px}
.signup .btn{position:absolute;left:687px;top:24px;width:84px;height:30px;background:var(--yellow);font-family:"Roboto Condensed",sans-serif;font-weight:700;font-size:13px;text-align:center;line-height:30px;color:#2a1b00}
.dest-title{position:absolute;top:738px;left:0;width:821px;text-align:center;font-size:16px;font-weight:300;color:#222}
.dest{position:absolute;top:784px;list-style:none;font-size:11px;line-height:19.7px;color:#333}
.dest li{height:19.7px}
.c1{left:55px}.c2{left:244px}.c3{left:456px}.c4{left:638px}
.footer{position:absolute;top:1121px;left:0;width:821px;border-top:1px solid var(--rule);height:79px}
.footer .copy{position:absolute;left:36px;top:26px;font-size:8.5px;color:#333}
.footer .addr{position:absolute;left:36px;top:46px;font-size:8.2px;color:#333}
.badges{position:absolute;left:672px;top:25px;display:flex;gap:16px;align-items:center}
</style>
</head>
<body>
<div class="page">
  <div class="topbar">Meadow Voyages takes pride in excelling as a premier leisure experience company
    <div class="social"><span>BLOGLEAF</span><span>FRIENDHUB</span><span>CHIRPER</span></div>
  </div>
  <header class="nav">
    <div class="brand">MEADOW VOYAGES</div>
    <nav class="menu"><span>ABOUT US</span><span>TOURS</span><span>ACCOUNT</span></nav>
    <div class="member">Are you a member?<b>Register / Login</b></div>
    <div class="offers">SPECIAL OFFERS</div>
  </header>
  <section class="hero" role="img" aria-label="Pride of lions walking along a dusty savanna track">
    <div class="hero-title">AFRICA</div>
    <div class="dots"><span></span><span></span><span></span><span></span></div>
    <div class="price"><small>From USD</small><strong>1,506</strong></div>
  </section>
  <section class="signup">
    <p>Stay upto to date about our special offers?</p>
    <div class="field">signup@example.com</div>
    <div class="btn">SIGN UP</div>
  </section>
  <h2 class="dest-title">Our designations:</h2>
  <ul class="dest c1">
    <li>close</li><li>Americas</li><li>Argentina | SHOP</li><li>Brasil | SHOP</li><li>Canada (EN) | SHOP</li><li>Canada (FR) | SHOP</li><li>Chile | SHOP</li><li>Colombia | SHOP</li><li>Latinoamérica</li><li>México | SHOP</li><li>Perú | SHOP</li><li>United States</li><li>Asia Pacific</li><li>Australia &nbsp;| SHOP</li><li>China | SHOP</li><li>Hong Kong</li>
  </ul>
  <ul class="dest c2">
    <li>India</li><li>Indonesia</li><li>Japan | SHOP</li><li>Korea | SHOP</li><li>Malaysia | SHOP</li><li>New Zealand | SHOP</li><li>Phillipines | SHOP</li><li>Singapore | SHOP</li><li>Taiwan</li><li>Thailand &nbsp;| SHOP</li><li>Vietnam</li><li>Europe</li><li>Baltics</li><li>Belgium | SHOP</li><li>Czech Republic | SHOP</li><li>Danmark | SHOP</li>
  </ul>
  <ul class="dest c3">
    <li>Germany | SHOP</li><li>Ελλάδα</li><li>Espana | SHOP</li><li>France | SHOP</li><li>Italia | SHOP</li><li>Ireland | SHOP</li><li>Magyarország</li><li>Nederland | SHOP</li><li>Norge</li><li></li><li>Austria | SHOP</li><li>Polska | SHOP</li><li>Portugal</li><li>Россия | SHOP</li><li>Switzerland</li>
  </ul>
  <ul class="dest c4">
    <li>Slovakia | SHOP</li><li>Suomi | SHOP</li><li>Sverige | SHOP</li><li>Türkiye | SHOP</li><li>United Kingdom | SHOP</li><li>Middle East</li><li>Middle East</li><li></li><li>Africa</li><li>South Africa</li><li></li><li>Other</li><li>stridewear.com</li>
  </ul>
  <footer class="footer">
    <div class="copy">©2008-2014 MEADOW VOYAGES LTD, ALL RIGHTS RESERVED</div>
    <div class="addr">Corporate Office: 48 Orchard Lane, Fairbrook, NJ, 08999 | Phone: 555-210-4417 | Fax: 555-210-4480 | Toll Free: 1-888-555-0142 or 1-877-555-0199</div>
    <div class="badges">
      <svg width="28" height="28" aria-hidden="true"><circle cx="14" cy="14" r="13" fill="#2d5d9c"/></svg>
      <svg width="28" height="28" aria-hidden="true"><circle cx="14" cy="14" r="13" fill="#7a4a2a"/></svg>
      <svg width="40" height="22" aria-hidden="true"><rect x="1" y="1" width="38" height="20" fill="#e9e3c8"/></svg>
    </div>
  </footer>
</div>
</body>
</html>
```